Business Card Design Project

Name Martin Hollowell
Company Pinebrook Hazard Recovery Crew
address 27/3 Korvenado street
Wattle Hollow
Carrowvale Eastmere
Marendia 5823,
0487352916

Things that we do Mould inspection and Remediation,
Crime and Trauma Scene Cleanup and Decontamination
Drug lab Decontamination and needle cleanups.
Odor control
Air quality Testing and swabs,
latest equipment
Hydroxyl machines, ozone machines ,Sterilising lights ,Comercial Steam machines ,
Thermal imaging, Bacteria testing equipment
Fully trained personel

Reason: One day is not enough time to get designs i dont why the Current deadline is only one day

I do not need vanta wipe in the cards, that was only a sample, The Business name isĀ 

Pinebrook Hazard Recovery Crew.

Target Market(s)

Government agencies ,Police and real-estates, housing companies, Coroners

Industry/Entity Type

Business

Requirements
Must have
• Must tell what we are about
Nice to have
• raised letters or good background

```html
<!DOCTYPE html>
<html lang="en">
<head>
<meta charset="utf-8">
<title>Pinebrook Hazard Recovery Crew – Business Card</title>
<link rel="stylesheet" href="https://fonts.googleapis.com/css2?family=Open+Sans:wght@400;700&display=swap">
<style>
  :root {
    --page-bg: #e9e6e1;
    --card-black: #000000;
    --hazard-yellow: #fff200;
    --text-white: #ffffff;
    --emblem-tone: #1e1e1e;
    --card-shadow: rgba(0, 0, 0, 0.45);
  }
  * { box-sizing: border-box; margin: 0; padding: 0; }
  html, body {
    width: 1200px;
    height: 1000px;
    overflow: hidden;
    background: var(--page-bg);
    font-family: "Open Sans", Arial, sans-serif;
    color: var(--text-white);
  }
  .sheet {
    position: relative;
    width: 1200px;
    height: 1000px;
  }
  .card {
    position: absolute;
    top: 672px;
    width: 538px;
    height: 300px;
    background: var(--card-black);
    box-shadow: 2px 4px 10px var(--card-shadow);
    overflow: hidden;
  }
  .card--front { left: 45px; }
  .card--back { left: 617px; }

  /* Front */
  .hazard-band {
    position: absolute;
    left: 0;
    width: 100%;
    height: 30px;
    display: block;
  }
  .hazard-band--top { top: 0; }
  .hazard-band--bottom { bottom: 0; }

  .company-stack {
    position: absolute;
    left: 25px;
    top: 98px;
    font-weight: 700;
    font-size: 19px;
    line-height: 26px;
  }
  .contact-block {
    position: absolute;
    right: 21px;
    top: 76px;
    text-align: right;
    font-weight: 700;
  }
  .contact-block .person-name {
    font-size: 23px;
    line-height: 34px;
    margin-bottom: 4px;
  }
  .contact-block .phone {
    font-size: 16px;
    line-height: 24px;
    letter-spacing: 0.5px;
    margin-bottom: 1px;
  }
  .contact-block .address-line {
    font-size: 14.5px;
    line-height: 23.7px;
  }

  /* Back */
  .emblem-area {
    position: absolute;
    left: 115px;
    top: 20px;
    width: 310px;
    height: 300px;
    border-radius: 50%;
    background: radial-gradient(circle, var(--emblem-tone) 0%, rgba(30,30,30,0.5) 50%, rgba(0,0,0,0) 70%);
  }
  .back-title {
    position: absolute;
    top: 16px;
    left: 0;
    width: 100%;
    text-align: center;
    font-size: 19px;
    font-weight: 400;
  }
  .service-list {
    position: absolute;
    left: 19px;
    top: 72px;
    list-style: none;
    font-size: 12.5px;
    line-height: 22px;
  }
  .equipment-list {
    position: absolute;
    right: 18px;
    top: 154px;
    list-style: none;
    text-align: right;
    font-size: 12.5px;
    line-height: 25.5px;
  }
  .trained-note {
    position: absolute;
    top: 253px;
    left: 0;
    width: 100%;
    text-align: center;
    font-size: 20px;
  }
</style>
</head>
<body>
<main class="sheet">

  <section class="card card--front" aria-label="Card front">
    <svg class="hazard-band hazard-band--top" viewBox="0 0 538 30" preserveAspectRatio="none" aria-hidden="true">
      <defs>
        <pattern id="hazardStripes" width="42.5" height="30" patternUnits="userSpaceOnUse" x="4">
          <polygon points="10,0 30,0 22,30 2,30" fill="var(--hazard-yellow)"/>
        </pattern>
      </defs>
      <rect width="538" height="30" fill="url(#hazardStripes)"/>
    </svg>

    <div class="company-stack">
      Pinebrook<br>Hazard<br>Recovery<br>Crew
    </div>

    <div class="contact-block">
      <div class="person-name">Martin Hollowell</div>
      <div class="phone">0487352916</div>
      <div class="address-line">27/3 Korvenado street</div>
      <div class="address-line">Wattle Hollow</div>
      <div class="address-line">Carrowvale Eastmere</div>
      <div class="address-line">Marendia 5823</div>
    </div>

    <svg class="hazard-band hazard-band--bottom" viewBox="0 0 538 30" preserveAspectRatio="none" aria-hidden="true">
      <rect width="538" height="30" fill="url(#hazardStripes)"/>
    </svg>
  </section>

  <section class="card card--back" aria-label="Card back">
    <div class="emblem-area" role="img" aria-label="Faint hazard emblem decoration behind the text"></div>

    <h2 class="back-title">Pinebrook Hazard Recovery Crew</h2>

    <ul class="service-list">
      <li>Crime and Trauma Scene Cleanup and Decontamination;</li>
      <li>Drug lab Decontamination and needle cleanups;</li>
      <li>Odor control;</li>
      <li>Air quality Testing and swabs.</li>
    </ul>

    <ul class="equipment-list">
      <li>Hydroxyl machines, ozone machines,</li>
      <li>Sterilising lights, Comercial Steam machines,</li>
      <li>Thermal imaging, Bacteria testing equipment</li>
    </ul>

    <p class="trained-note">Fully trained personel</p>
  </section>

</main>
</body>
</html>
```